CEO of company needs clear business card that stands out from the rest

I need a clear business card (standard credit card size) for the CEO/Founder of our company...Brightfield Counseling. We would like to see designs that use our logo colors, which are khaki, chocolate brown, and gray. The card should be an edgy design, maybe where half the card is transparent with curves on the card, or a textured card where the logo is transparent, I don't care much for white cards. The final design should communicate a funky, edgy, and modern look, as well as stand out to have the "WOW" factor. The information we need on the card would be Name, Title, Toll free number, Phone Number, address, email address, and website.

*PLEASE SEND FRONT AND BACK OF CARDS

Card is two sided front and back please give us your front and back designs

The card should be an edgy design, maybe where half the card is transparent with curves on the card, or a textured card where the logo is transparent, I don't care much for white cards. The final design should communicate a funky, edgy, and modern look, as well as stand out to have the "WOW" factor.

Please follow these guidelines for the card

SPECS (card):

2.125 (h) x 3.375 (w) card size after cut

2.375 (h) x 3.625 (w) card with bleed

300 dpi

cmyk

1/8 bleed

allow 1/8 border for live area

I will also attached the pdf for the information listed above which includes a diagram of the card

 

All the cards need to have rounded edges

I just updated a card as an example of how you can use different fonts on a single business card, look how the name is written in script, so what I am saying is make this a card you will be proud to design and put it in your portfolio 

Reason: this race is really close and I am working with 2 designers to fine tune their designs and the weekend is slowing us down

• Our Logo
MUST HAVE PARTS OF CARD THAT ARE TRANSPARENT. See ideas that are attached.
Card is two sided front and back
• The final design should communicate a funky, edgy, and modern look, as well as stand out to have the "WOW" factor. The information we need on the card would be Name, Title, Toll free number, Phone Number, address, email address, and website.

```html
<!DOCTYPE html>
<html lang="en">
<head>
<meta charset="utf-8">
<title>Brightfield Counseling – Business Card</title>
<link rel="stylesheet" href="https://fonts.googleapis.com/css2?family=Arimo:wght@400;700&display=swap">
<style>
  :root {
    --stage: #3a3624;
    --choc-dark: #4a200c;
    --choc: #6e3417;
    --choc-light: #8a4722;
    --gold: #f6b52e;
    --gold-soft: #ffd77a;
    --khaki-light: #d8dc8a;
    --khaki-dark: #5f6b24;
    --cream: #f3e6d6;
    --white: #ffffff;
  }
  * { margin: 0; padding: 0; box-sizing: border-box; }
  html, body { width: 1200px; height: 958px; overflow: hidden; }
  body {
    background: var(--stage);
    font-family: "Arimo", Arial, sans-serif;
    position: relative;
  }
  .card {
    position: absolute;
    left: 342px;
    width: 551px;
    height: 336px;
    border-radius: 14px;
    background: radial-gradient(ellipse at 35% 40%, var(--choc-light), var(--choc) 55%, var(--choc-dark));
    overflow: hidden;
    box-shadow: 0 6px 18px rgba(0,0,0,.35);
  }
  .card--front { top: 100px; }
  .card--back { top: 486px; }
  .card__frame {
    position: absolute; inset: 9px;
    border: 1px solid rgba(255, 215, 150, .35);
    border-radius: 9px;
  }
  .card__swoosh { position: absolute; inset: 0; width: 100%; height: 100%; }
  .emblem {
    position: absolute;
    width: 180px; height: 180px;
    border-radius: 50%;
    background: radial-gradient(circle at 55% 40%, var(--khaki-light), #9ba446 50%, var(--khaki-dark));
    box-shadow: 0 0 0 2px rgba(246,181,46,.25);
  }
  .card--front .emblem { left: 37px; top: 78px; }
  .card--back .emblem { left: 329px; top: 66px; }
  .brand-panel {
    position: absolute;
    left: 331px; top: 14px;
    width: 177px; height: 178px;
    background: var(--white);
    display: flex; align-items: center; justify-content: center;
    padding: 12px;
  }
  .brand-panel__name {
    font-weight: 700;
    font-size: 20px;
    line-height: 1.2;
    color: var(--choc);
    text-align: center;
  }
  .contact-strip {
    position: absolute;
    left: 204px; top: 294px;
    display: flex; gap: 26px;
    font-size: 10px;
    color: var(--cream);
    opacity: .8;
  }
  .holder { position: absolute; left: 41px; top: 146px; color: var(--cream); }
  .holder__name { font-size: 26px; font-weight: 400; }
  .holder__title { font-size: 9px; margin-top: 4px; opacity: .8; }
  .holder__address { font-size: 9px; margin-top: 16px; line-height: 1.45; opacity: .85; }
  .holder__lines {
    margin-left: 69px; margin-top: 10px;
    font-size: 9px; line-height: 1.45; opacity: .85;
    display: grid; grid-template-columns: 46px auto;
  }
  .holder__email {
    margin-left: 69px;
    font-size: 9px; line-height: 1.45; opacity: .85;
  }
  .holder__web {
    position: absolute; left: 41px; top: 300px;
    font-size: 9px; font-weight: 700; color: var(--cream); opacity: .9;
  }
</style>
</head>
<body>

<section class="card card--front" aria-label="Card front">
  <svg class="card__swoosh" viewBox="0 0 551 336" aria-hidden="true">
    <path d="M300 0 C 265 120, 215 230, 118 336 L 136 336 C 232 230, 282 120, 316 0 Z" fill="var(--gold)"/>
    <path d="M322 0 C 290 120, 240 230, 148 336" fill="none" stroke="var(--gold-soft)" stroke-width="1.2" opacity=".6"/>
  </svg>
  <div class="card__frame"></div>
  <div class="emblem" role="img" aria-label="Round brand emblem area"></div>
  <div class="brand-panel">
    <span class="brand-panel__name">Brightfield Counseling</span>
  </div>
  <div class="contact-strip">
    <span>1.800.000.0000</span>
    <span>000.000.0000</span>
    <span>www.brightfieldcounseling.com</span>
  </div>
</section>

<section class="card card--back" aria-label="Card back">
  <svg class="card__swoosh" viewBox="0 0 551 336" aria-hidden="true">
    <path d="M240 0 C 282 100, 306 210, 300 336 L 316 336 C 322 210, 298 100, 256 0 Z" fill="var(--gold)"/>
    <path d="M228 0 C 270 100, 294 210, 288 336" fill="none" stroke="var(--gold-soft)" stroke-width="1.2" opacity=".6"/>
  </svg>
  <div class="card__frame"></div>
  <div class="emblem" role="img" aria-label="Round brand emblem area"></div>
  <div class="holder">
    <div class="holder__name">John Smith</div>
    <div class="holder__title">CEO</div>
    <div class="holder__address">your complete address here<br>your complete address here</div>
    <div class="holder__lines">
      <span>toll free</span><span>1.800.000.0000</span>
      <span>phone</span><span>000.000.0000</span>
    </div>
    <div class="holder__email">john@brightfieldcounseling.com</div>
  </div>
  <div class="holder__web">www.brightfieldcounseling.com</div>
</section>

</body>
</html>
```